Eye Catching Business Card for Optometrist

We've recently refreshed our logo and now we need a fresh and bold look for our business cards. We provide progressive ways to improve people's vision and protect their eye health.

Use our new logo as guidance into the colors to use. As far as style goes, I love how bold and eye catching the card is for Lanternfly Studio. Feel free to use your creative judgement.

Tagline: "Sharper sight for every day."

pertinent info to include:

Dr. Martin Sowerby
Optometrist

2857 Bramwell Ridge Blvd #217
Larkspur Falls, MO 65012
(555) 382-7190

marty@brightlenshomeoptics.example
www.brightlenshomeoptics.example

```html
<!DOCTYPE html>
<html lang="en">
<head>
<meta charset="utf-8">
<title>Brightlens Home Optics – Business Card</title>
<link rel="stylesheet" href="https://fonts.googleapis.com/css2?family=Ubuntu:wght@400;500;700&display=swap">
<style>
  :root {
    --backdrop: #d9d9d9;
    --brand-red: #b0102a;
    --brand-red-deep: #9c0c24;
    --brand-tan: #c9ae85;
    --brand-gold: #d8b877;
    --paper: #f7f6f3;
    --ink: #1f1f1f;
    --ink-soft: #3a3a3a;
  }
  * { box-sizing: border-box; margin: 0; padding: 0; }
  html, body {
    width: 1200px;
    height: 1000px;
    overflow: hidden;
  }
  body {
    background: var(--backdrop);
    font-family: "Ubuntu", sans-serif;
    position: relative;
  }
  .card {
    position: absolute;
    left: 320px;
    width: 560px;
    height: 320px;
    border-radius: 3px;
  }

  /* Front */
  .card--front {
    top: 130px;
    background: linear-gradient(135deg, var(--brand-red-deep), var(--brand-red));
    display: flex;
    flex-direction: column;
    align-items: center;
    justify-content: center;
    text-align: center;
  }
  .wordmark {
    display: flex;
    align-items: center;
    gap: 14px;
    color: #ffffff;
    font-weight: 700;
    font-size: 34px;
    line-height: 1.05;
    text-transform: uppercase;
    letter-spacing: 0.5px;
  }
  .wordmark__square {
    width: 30px;
    height: 30px;
    background: var(--brand-tan);
    flex: none;
  }
  .tagline {
    margin-top: 26px;
    color: var(--brand-gold);
    font-weight: 700;
    text-transform: uppercase;
    line-height: 1.05;
  }
  .tagline__lead { display: block; font-size: 17px; letter-spacing: 0.6px; }
  .tagline__main { display: block; font-size: 27px; letter-spacing: 0.3px; }

  /* Back */
  .card--back {
    top: 540px;
    background: var(--paper);
    display: flex;
    align-items: center;
  }
  .card__brand {
    width: 252px;
    padding-left: 30px;
    display: flex;
    align-items: center;
    gap: 10px;
    color: var(--brand-red);
    font-weight: 700;
    font-size: 25px;
    line-height: 1.1;
    text-transform: uppercase;
  }
  .card__brand-square {
    width: 22px;
    height: 22px;
    background: var(--brand-tan);
    flex: none;
  }
  .card__divider {
    width: 2px;
    height: 178px;
    background: var(--brand-red);
    margin-right: 30px;
  }
  .contact { color: var(--ink-soft); font-size: 14.5px; line-height: 1.35; }
  .contact__name { color: var(--ink); font-size: 21px; font-weight: 700; }
  .contact__role { font-size: 11.5px; margin-bottom: 16px; }
  .contact__address { margin-bottom: 8px; }
  .contact__line { margin-bottom: 8px; }
</style>
</head>
<body>

  <section class="card card--front" aria-label="Business card front">
    <div class="wordmark">
      <span class="wordmark__square" aria-hidden="true"></span>
      <span>Brightlens<br>Home Optics</span>
    </div>
    <p class="tagline">
      <span class="tagline__lead">Sharper sight for</span>
      <span class="tagline__main">Every day</span>
    </p>
  </section>

  <section class="card card--back" aria-label="Business card back">
    <div class="card__brand">
      <span class="card__brand-square" aria-hidden="true"></span>
      <span>Brightlens<br>Home Optics</span>
    </div>
    <div class="card__divider" aria-hidden="true"></div>
    <div class="contact">
      <p class="contact__name">Dr. Martin Sowerby</p>
      <p class="contact__role">Optometrist</p>
      <p class="contact__address">2857 Bramwell Ridge Blvd #217<br>Larkspur Falls, MO 65012</p>
      <p class="contact__line">(555) 382-7190</p>
      <p class="contact__line">marty@brightlenshomeoptics.example</p>
      <p class="contact__line">www.brightlenshomeoptics.example</p>
      <p>www.brightlenshomeoptics.example</p>
    </div>
  </section>

</body>
</html>
```